International Lifestyle Real Estate Brokerage Needs Eye Catching Website

We need a new website for a cutting edge / dynamic real estate startup, Pinecrest Realty, that will serve as a concierge brokerage to assist cold weather residents with the research, selection, financing and purchase of vacation / retirement properties in warm weather climates in the US and then globally. We will have personally vetted all properties to insure that our clients are only getting the best of the best with no hidden surprises.

** The website design will ultimately need to be coded into a wordpress theme.

We are not locked into any specific colour scheme but would prefer something warm vs cold as that is really the lifestyle we are selling. We like lots of white negative space and hope to allow high end photography to provide most of the pop in colour.

I have attached mock up wire frames to demonstrate desired functionality for three pages we need designed

1) Home Page
2) Market Profile (City overview and developments)
3) Community Profile Page (Individual development profile)

I have also included .ai file for the logo. Not locked into red.

Final design should communicate excitement, lifestyle while maintaining an air of professionalism and reliability. We have developed over 30 sites and have high expectations for the winning design.

Regards,
Dan
Updates

Project Deadline Extended Reason: Hello,I have been called away from this project for the past couple of weeks and have been unable to get together with the people involved to get a consensus on direction forward. Apologies for the delay - we are still very much committed to moving forward.Regards,Dan Added Wednesday, July 6, 2016

Target Market(s)

Canadian and Northern US residents looking to purchase vacation or retirement real estate in warmer climates, initially in the US, but eventually Internationally.

Industry/Entity Type

Real Estate

Contact Information for Business Card

Names for Business Cards

Dan Whitford
705.555.2147
dan@pinecrestrealty-example.ca

Coding

Coded - Design and coding required

Number of Pages Required

3 page

Font styles to use
Serif
Sans Serif

Requirements
Must have
• See wireframe documents uploaded.
• Site design will ultimately be coded into a child theme to function on a selected wordpress theme. If the designer has a Wordpres Theme in mind that would be compatible with the design we would appreciate that information.
Nice to have
• See wireframe documents uploaded. Prefer clean, modern site, white negative space, bold photography will add most of the colour and pop.
Should not have
• Anything cartoony or sophmoric.

```html
<!DOCTYPE html>
<html lang="en">
<head>
<meta charset="utf-8">
<title>Pinecrest Realty — Home</title>
<link rel="stylesheet" href="https://fonts.googleapis.com/css2?family=Open+Sans:wght@300;400;600;700&display=swap">
<style>
:root{
  --red:#e8353b;
  --navy:#2f3a4b;
  --navy-deep:#2b3545;
  --gray-bg:#e7e7e7;
  --white:#ffffff;
  --ink:#222831;
  --muted:#6b6f75;
  --line:#c9cbd0;
}
*{box-sizing:border-box;margin:0;padding:0}
html,body{width:1200px;height:3448px;overflow:hidden}
body{font-family:"Open Sans",Arial,sans-serif;color:var(--ink);background:var(--white);position:relative}
section,header,footer{position:relative;width:1200px;overflow:hidden}
.abs{position:absolute}
.btn-red{background:var(--red);color:var(--white);font-size:11px;font-weight:600;text-transform:uppercase;display:flex;align-items:center;justify-content:center;letter-spacing:.5px}
.btn-navy{background:var(--navy);color:var(--white);font-size:9px;font-weight:600;text-transform:uppercase;display:flex;align-items:center;justify-content:center}

/* Hero */
.hero{height:602px}
.hero-photo{position:absolute;inset:0;background:linear-gradient(180deg,#7f8a94 0%,#9a8a6e 45%,#b58a4f 62%,#5e7a86 78%,#3f6d7f 100%)}
.hero-shade{position:absolute;inset:0;background:rgba(30,35,45,.18)}
.menu-toggle{left:161px;top:22px;width:42px;height:30px}
.login{left:963px;top:23px;width:75px;height:28px;font-size:12px}
.brand{left:0;width:1200px;top:186px;text-align:center;color:var(--white);font-size:34px;font-weight:600;letter-spacing:6px}
.tagline{left:0;width:1200px;top:294px;text-align:center;color:var(--white);font-size:38px;font-weight:300;letter-spacing:1px}
.search{left:214px;top:361px;width:770px;height:44px;background:var(--white);display:flex;align-items:center;padding:0 26px;font-size:13px;color:#666}
.search svg{position:absolute;right:20px;top:11px}

/* Services */
.services{height:658px;background:var(--gray-bg)}
.section-title{position:absolute;left:0;width:1200px;text-align:center;font-weight:300;font-size:40px;color:var(--ink)}
.services .section-title{top:66px}
.service-card{position:absolute;top:180px;width:238px;height:280px;text-align:center}
.service-card.is-active{border:1.5px solid #f0a0a3;border-radius:4px}
.service-card svg{margin-top:30px}
.service-card h3{font-size:12px;font-weight:600;line-height:19px;margin-top:14px;text-transform:uppercase}
.service-card p{font-size:10px;line-height:16px;color:var(--muted);width:190px;margin:12px auto 0}
.service-card .btn-navy,.service-card .btn-red{width:86px;height:26px;margin:26px auto 0;font-size:9px}
.register{left:466px;top:527px;width:268px;height:53px;border:2px solid var(--red);display:flex;align-items:center;justify-content:center;font-size:20px;letter-spacing:.5px}

/* Featured developments */
.developments{height:501px}
.dev-photo{position:absolute;inset:0;background:linear-gradient(180deg,#45536a 0%,#5b6a80 50%,#3c4a60 100%)}
.developments .section-title{top:60px;color:var(--white)}
.dev-intro{top:128px;left:0;width:1200px;text-align:center;color:var(--white);font-size:16px;line-height:22px}
.dev-panel{left:143px;top:184px;width:916px;height:225px;background:rgba(200,205,215,.35)}
.dev-item{position:absolute;top:18px;width:212px}
.dev-item .photo{height:148px;border:3px solid var(--white)}
.dev-item span{display:block;text-align:center;color:var(--white);font-size:15px;margin-top:10px}
.pager{left:574px;top:434px;display:flex;gap:6px}
.pager span{width:24px;height:24px;border:1.5px solid var(--white);border-radius:50%;display:flex;align-items:center;justify-content:center}

/* Markets */
.markets{height:979px;background:var(--gray-bg)}
.markets .section-title{top:78px}
.tab{position:absolute;top:170px;height:46px;display:flex;align-items:center;justify-content:center;font-size:11px;font-weight:600;border:1.5px solid #8d97a5;color:var(--navy)}
.tab.is-current{background:var(--navy);color:var(--white);border-color:var(--navy)}
.market{position:absolute}
.market .photo{position:absolute;inset:0}
.market span{position:absolute;left:0;right:0;bottom:18px;text-align:center;color:var(--white);font-size:22px;text-shadow:0 1px 3px rgba(0,0,0,.5)}
.commitment{left:161px;top:800px;width:878px}
.commitment h2{font-size:17px;font-weight:700;letter-spacing:.3px}
.commitment p{font-size:11px;line-height:19px;color:var(--muted);margin-top:8px}
.commitment .btn-red{width:88px;height:26px;margin-top:14px;font-size:9px}

/* Blog */
.blog{height:235px;background:var(--white)}
.blog .section-title{top:52px;font-size:30px}
.post{position:absolute;top:122px;width:380px;display:flex;gap:14px}
.post .thumb{width:60px;height:60px;flex:none}
.post h3{font-size:11px;font-weight:700;text-transform:uppercase;margin-top:2px}
.post p{font-size:10px;line-height:14px;color:var(--muted);margin-top:6px}
.post a{font-size:8px;color:var(--red);text-decoration:underline;text-transform:uppercase}

/* Newsletter */
.newsletter{height:152px;background:var(--navy)}
.newsletter h2{left:161px;top:64px;color:var(--white);font-size:15px;font-weight:400;text-transform:uppercase}
.newsletter .field{left:462px;top:54px;width:577px;height:44px;background:var(--white);border-radius:22px;font-size:9px;color:#777;display:flex;align-items:center;padding-left:24px;text-transform:uppercase}
.newsletter .submit{left:913px;top:54px;width:126px;height:44px;border-radius:22px;font-size:13px;font-weight:700}

/* Contact bar */
.contact{height:92px;background:var(--white)}
.contact .call{left:161px;top:34px;font-size:17px}
.contact .touch{left:724px;top:34px;font-size:17px}
.social{left:862px;top:30px;display:flex;gap:18px}
.social span{width:30px;height:30px;border-radius:50%}

/* Footer */
.site-footer{height:229px;background:var(--navy-deep);color:var(--white)}
.site-footer .brand{top:72px;font-size:26px;letter-spacing:5px}
.footer-nav{left:0;width:1200px;top:156px;display:flex;justify-content:center;gap:0;font-size:11px}
.footer-nav a{color:var(--white);text-decoration:none;padding:0 22px;border-left:1px solid rgba(255,255,255,.6);line-height:12px}
.footer-nav a:first-child{border-left:none}
.footer-url{left:0;width:1200px;top:180px;text-align:center;font-size:8px;color:#8d96a3}
.to-top{left:587px;top:201px;width:24px;height:24px;border:1.5px solid var(--white);border-radius:50%;display:flex;align-items:center;justify-content:center}
</style>
</head>
<body>

<header class="hero">
  <div class="hero-photo" role="img" aria-label="Aerial photo of a waterfront city skyline at golden hour"></div>
  <div class="hero-shade"></div>
  <svg class="abs menu-toggle" viewBox="0 0 42 30" aria-label="Menu"><rect y="0" width="42" height="4" fill="#fff"/><rect y="13" width="42" height="4" fill="#fff"/><rect y="26" width="42" height="4" fill="#fff"/></svg>
  <div class="abs login btn-red">Login</div>
  <div class="abs brand">PINECREST REALTY</div>
  <h1 class="abs tagline">LIFE IS TOO SHORT TO BE COLD</h1>
  <div class="abs search">Where Do You Want to Play in The Sunshine ?
    <svg width="22" height="22" viewBox="0 0 22 22"><circle cx="9" cy="9" r="6.5" fill="none" stroke="#e8353b" stroke-width="2.5"/><line x1="14" y1="14" x2="20" y2="20" stroke="#e8353b" stroke-width="3"/></svg>
  </div>
</header>

<section class="services">
  <h2 class="section-title">WE’RE SERVICE PROVIDED</h2>

  <div class="service-card" style="left:132px">
    <svg width="30" height="26" viewBox="0 0 30 26"><polyline points="2,2 2,24 28,24" fill="none" stroke="#333" stroke-width="2"/><polyline points="5,19 12,11 17,15 26,6" fill="none" stroke="#333" stroke-width="2"/></svg>
    <h3>Dynamic<br>Real Estate</h3>
    <p>Our team vets every listing so you buy warm weather homes with no hidden surprises.</p>
    <div class="btn-navy">Learn More</div>
  </div>
  <div class="service-card is-active" style="left:363px">
    <svg width="30" height="30" viewBox="0 0 30 30"><circle cx="15" cy="16" r="11" fill="none" stroke="#e8353b" stroke-width="2.4"/><path d="M15 5 V16 H26" fill="none" stroke="#e8353b" stroke-width="2.4"/></svg>
    <h3>Dynamic<br>Real Estate</h3>
    <p>We guide the research, selection and financing of your vacation or retirement home.</p>
    <div class="btn-red">Learn More</div>
  </div>
  <div class="service-card" style="left:598px">
    <svg width="32" height="28" viewBox="0 0 32 28"><path d="M8 21 H7 A6 6 0 0 1 8 9 A8 8 0 0 1 24 9 A6 6 0 0 1 25 21 H24" fill="none" stroke="#333" stroke-width="2"/><path d="M16 26 V13 M11 17 L16 12 L21 17" fill="none" stroke="#333" stroke-width="2"/></svg>
    <h3>Dynamic<br>Real Estate</h3>
    <p>Clear market insight on sunny cities, from local taxes to the best new communities.</p>
    <div class="btn-navy">Learn More</div>
  </div>
  <div class="service-card" style="left:832px">
    <svg width="28" height="28" viewBox="0 0 28 28"><path d="M12 4 H3 V25 H24 V16" fill="none" stroke="#333" stroke-width="2"/><path d="M16 3 H25 V12 M25 3 L12 16" fill="none" stroke="#333" stroke-width="2"/></svg>
    <h3>Dynamic<br>Real Estate</h3>
    <p>Personal concierge support from your first search right through to closing day.</p>
    <div class="btn-navy">Learn More</div>
  </div>

  <div class="abs register">REGISTER CTA</div>
</section>

<section class="developments">
  <div class="dev-photo" role="img" aria-label="Faded photo of downtown office towers"></div>
  <h2 class="section-title">FEATURED DEVELOPMENTS</h2>
  <p class="abs dev-intro">Hand picked new communities in the warmest markets, each one<br>visited and vetted by our team before we list it.</p>
  <div class="abs dev-panel">
    <div class="dev-item" style="left:19px"><div class="photo" role="img" aria-label="Photo of a modern apartment block" style="background:linear-gradient(180deg,#9fc3e6,#d9c8a8 60%,#7d9a5c)"></div><span>Lorem Ipsum</span></div>
    <div class="dev-item" style="left:244px"><div class="photo" role="img" aria-label="Photo of a city with highway interchange" style="background:linear-gradient(180deg,#8fb6dc,#b7c2cc 55%,#6f7c86)"></div><span>Lorem Ipsum</span></div>
    <div class="dev-item" style="left:469px"><div class="photo" role="img" aria-label="Photo of a wave shaped building at dusk" style="background:linear-gradient(180deg,#2f4a6e,#6b86a6 55%,#c9a874)"></div><span>Lorem Ipsum</span></div>
    <div class="dev-item" style="left:685px"><div class="photo" role="img" aria-label="Photo of a glass office building" style="background:linear-gradient(160deg,#4f8fd0,#a9cbe8 55%,#e7eef4)"></div><span>Lorem Ipsum</span></div>
  </div>
  <div class="abs pager">
    <span><svg width="10" height="10" viewBox="0 0 10 10"><polyline points="6.5,1.5 3,5 6.5,8.5" fill="none" stroke="#fff" stroke-width="1.6"/></svg></span>
    <span><svg width="10" height="10" viewBox="0 0 10 10"><polyline points="3.5,1.5 7,5 3.5,8.5" fill="none" stroke="#fff" stroke-width="1.6"/></svg></span>
  </div>
</section>

<section class="markets">
  <h2 class="section-title">FEATURED MARKETS</h2>
  <div class="tab is-current" style="left:363px;width:161px">UNITED STATES</div>
  <div class="tab" style="left:531px;width:129px">MEXICO</div>
  <div class="tab" style="left:664px;width:173px">SOUTH AMERICA</div>

  <div class="market" style="left:161px;top:264px;width:278px;height:230px"><div class="photo" role="img" aria-label="Photo of a couple relaxing on a lawn by a house" style="background:linear-gradient(180deg,#8aa4b8,#9a7a5c 50%,#6b8f3e)"></div><span>Orlando</span></div>
  <div class="market" style="left:460px;top:264px;width:278px;height:230px"><div class="photo" role="img" aria-label="Photo of a woman in front of a lit apartment tower at night" style="background:linear-gradient(180deg,#2a2c30,#5a5650 50%,#8a8378)"></div><span>Naples</span></div>
  <div class="market" style="left:761px;top:264px;width:278px;height:230px"><div class="photo" role="img" aria-label="Photo of a historic square with a statue" style="background:linear-gradient(180deg,#a9c4e0,#b9a98e 55%,#8a8172)"></div><span>Fort Meyers</span></div>
  <div class="market" style="left:161px;top:520px;width:425px;height:232px"><div class="photo" role="img" aria-label="Photo of a family in front of a suburban home" style="background:linear-gradient(180deg,#c6d4e0,#b8bcc0 45%,#6f8a4a)"></div><span>Clearwater</span></div>
  <div class="market" style="left:614px;top:520px;width:425px;height:232px"><div class="photo" role="img" aria-label="Photo of a palm lined street with a yellow historic building" style="background:linear-gradient(180deg,#8eb3d8,#c9a655 50%,#5a7040)"></div><span>Asheville</span></div>

  <div class="abs commitment">
    <h2>OUR COMMITMENT</h2>
    <p>We help northern families find sunny homes they love. Every property we show has been visited by our team, checked for quality, and priced with care. From the first call to the final signature, we explain each step plainly and stay on your side. Our promise is simple: honest advice, trusted local partners, and a smooth move into the warm weather lifestyle you have earned.</p>
    <div class="btn-red">View More</div>
  </div>
</section>

<section class="blog">
  <h2 class="section-title">RECENT BLOG POSTS</h2>
  <article class="post" style="left:161px">
    <div class="thumb" role="img" aria-label="Author portrait photo" style="background:linear-gradient(180deg,#9fb4c6,#6f7f8c)"></div>
    <div><h3>Dynamic Real Estate Blog</h3><p>Five things to check before you buy a winter home in Florida this year.</p><a>View All</a></div>
  </article>
  <article class="post" style="left:669px">
    <div class="thumb" role="img" aria-label="House icon illustration" style="background:linear-gradient(180deg,#d77a4a,#3f6f8f)"></div>
    <div><h3>Dynamic Real Estate Blog</h3><p>How currency rates shape the real cost of a warm weather retirement.</p><a>View All</a></div>
  </article>
</section>

<section class="newsletter">
  <h2 class="abs">Subscribe Our Newsletter</h2>
  <div class="abs field">Your Email Address</div>
  <div class="abs submit btn-red">Submit</div>
</section>

<section class="contact">
  <div class="abs call">Call Us:  +0000001111, (+0000002222)</div>
  <div class="abs touch">Get In Touch</div>
  <div class="abs social" aria-label="Social links">
    <span style="background:#4b6fb0"></span><span style="background:#5a9fd6"></span><span style="background:#d9463a"></span><span style="background:#e86a5c"></span>
  </div>
</section>

<footer class="site-footer">
  <div class="abs brand">PINECREST REALTY</div>
  <nav class="abs footer-nav">
    <a>Home</a><a>About</a><a>Contact</a><a>Login</a><a>Saved</a><a>Search</a><a>Our Process</a><a>Resources</a>
  </nav>
  <div class="abs footer-url">http://www.pinecrestrealty-example.ca</div>
  <div class="abs to-top"><svg width="10" height="10" viewBox="0 0 10 10"><polyline points="1.5,6.5 5,3 8.5,6.5" fill="none" stroke="#fff" stroke-width="1.6"/></svg></div>
</footer>

</body>
</html>
```